Brochure Design Project

Need a new look. Customer wants to update 10 year old literature. Very similar "text content" and color scheme only. Need a new modern look. Clean fonts...maybe distressed fonts. Nice salon. Would like brochure to be consistent with their decor...possibly "curvey" graphics maybe simple die-cut if cost effective to produce. Use your imagination! Showed them some pixel harbor work that they liked the look of and I will share these details so you have a feel for the type of work we are looking for.
Updates

Reason: My customer has reviewed the art submissions and though she likes the ideas presented, she has indicated that she needs to stay more consistent with some other collateral which means she would prefer a more mono-chromatic (maybe two or three colors but not a full color glossy brochure. Keeping in mind that she would like a matte look please offer design selections. She has sent me some images of the other collateral she would possibly like to coordinate with which I can send via email upon request.

Target Market(s)

Salon Patrons

Industry/Entity Type

Salon

Requirements
Must have
• Packaged InDesign file upon completion so we can edit down the line(update prices etc.) High Res PDF with marks and bleeds. Must fit into No. 10 envelope(4.125" x 9.5") once folded...I am thinking 9x16 but am open to ideas.
Should not have
• photos...or limit

```html
<!DOCTYPE html>
<html lang="en">
<head>
<meta charset="utf-8">
<title>Vela Salon Spa – Tri-fold Brochure</title>
<link href="https://fonts.googleapis.com/css2?family=Arimo:wght@400;700&display=swap" rel="stylesheet">
<style>
:root{
  --olive:#c5bd66;
  --paper:#ffffff;
  --backdrop:#e2e2e2;
  --ink:#111111;
  --soft-text:#f4f1dc;
  --photo-dark:#3e3a36;
  --photo-mid:#8a7e70;
  --photo-light:#cdbfae;
}
*{box-sizing:border-box;margin:0;padding:0}
html,body{width:1200px;height:720px;overflow:hidden;background:var(--backdrop);font-family:"Arimo",Arial,sans-serif}
.canvas{position:relative;width:1200px;height:720px}

/* shared */
.photo-frame{position:absolute;background:var(--paper)}
.photo{position:absolute;left:8px;top:7px;right:8px;bottom:8px;
  background:linear-gradient(135deg,var(--photo-mid) 0%,var(--photo-dark) 45%,var(--photo-light) 100%)}
.brand{position:absolute;font-weight:700;color:var(--ink);line-height:1;text-align:center}
.brand span{display:block}

/* inside left panel */
.panel-about{position:absolute;left:45px;top:50px;width:348px;height:618px;background:var(--olive)}
.panel-about .photo-frame{left:29px;top:9px;width:135px;height:135px}
.panel-about .brand{left:180px;top:88px;width:140px;font-size:22px}
.about-title{position:absolute;left:111px;top:239px;width:140px;text-align:center;font-size:7px;color:var(--paper)}
.about-copy{position:absolute;left:111px;top:252px;width:126px;font-size:5.6px;line-height:7px;color:var(--soft-text);text-align:justify}
.about-copy p+p{margin-top:6px}
.policy-copy{position:absolute;left:24px;top:347px;width:302px;font-size:4.6px;line-height:5.4px;font-weight:700;color:var(--paper);text-align:justify}
.policy-copy p+p{margin-top:5px}

/* menu panel */
.panel-menu{position:absolute;left:401px;top:50px;width:347px;height:618px;background:var(--paper)}
.section-bar{position:absolute;width:128px;height:25px;background:var(--olive);color:var(--paper);
  font-size:11.5px;font-weight:700;line-height:25px;padding:0 17px}
.section-bar.right{left:219px;text-align:right}
.section-bar.left{left:0}
.note{position:absolute;font-size:3.2px;line-height:4.2px;font-weight:700;color:var(--ink);width:170px}
.note .gap{display:block;height:4.2px}
.menu-list{position:absolute;list-style:none;font-size:3.6px;font-weight:700;color:var(--ink)}
.menu-list li{display:flex;min-height:8.4px;line-height:4.3px}
.menu-list.col-left{left:18px;width:165px}
.menu-list.col-right{left:190px;width:150px}
.menu-list .item{width:81px;flex:none}
.menu-list.col-right .item{width:82px;font-size:4.3px}
.menu-list .price{flex:1}
.menu-list.col-right.facial-list li{min-height:10.8px}

.contact-box{position:absolute;left:173px;top:463px;width:174px;height:155px;background:var(--olive);text-align:center;color:var(--paper)}
.contact-box .brand{left:0;top:60px;width:174px;font-size:17px}
.contact-details{position:absolute;left:0;top:88px;width:174px;font-size:4.6px;line-height:5.6px}
.contact-details p{margin-bottom:6px}

/* front cover */
.panel-front{position:absolute;left:770px;top:50px;width:348px;height:154px;background:var(--olive)}
.panel-front .photo-frame{left:29px;top:16px;width:135px;height:138px}
.panel-front .brand{left:180px;top:72px;width:140px;font-size:22px}
.view-label{position:absolute;left:911px;top:212px;font-size:30px;color:var(--ink)}

/* folded in sleeve */
.sleeve-cover{position:absolute;left:770px;top:415px;width:348px;height:97px;background:var(--olive);overflow:hidden}
.sleeve-cover .photo-frame{left:29px;top:10px;width:135px;height:138px}
.sleeve-cover .brand{left:180px;top:66px;width:140px;font-size:22px}
.sleeve{position:absolute;left:766px;top:512px;width:358px;height:158px;background:var(--paper)}
.sleeve-edge{position:absolute;top:464px;width:5px;height:48px;background:var(--paper)}
.sleeve-edge.l{left:766px}
.sleeve-edge.r{left:1119px}
</style>
</head>
<body>
<div class="canvas">

  <section class="panel-about">
    <div class="photo-frame"><div class="photo" role="img" aria-label="Photo of a stylist trimming a client's hair"></div></div>
    <div class="brand"><span>Vela</span><span>Salon Spa</span></div>
    <h2 class="about-title">about us</h2>
    <div class="about-copy">
      <p>We are proud to have a team of wonderful people who are dedicated to self-growth, continued education and who have a strong desire to make people look and feel better. When you look good, you feel good.</p>
      <p>Our staff is committed to serving our guests as a team. We encourage trying our various technicians in order to enjoy all of their wonderful talents and ideas.</p>
    </div>
    <div class="policy-copy">
      <p>At vela salon and spa we are dedicated to making every visit a positive experience. Whether you are here for a day of pampering or for your regular salon appointment, our staff of experienced professionals are dedicated to meeting your every need. Escape the stresses of life and discover a new environment of relaxation and beauty.</p>
      <p>Communication is the key to a successful relationship with our clients. If at any time you are uncomfortable or dissatisfied in any way, we promise to make every effort to remedy the situation. Your opinions and comments are vital to the growth and success of our business and are greatly appreciated. If, for any reason, you are unhappy with a vela salon product, we will gladly exchange it with an equal product more suitable to your needs.</p>
      <p>To ensure you get the appointment time you most desire, we encourage you to book your next appointment before leaving. In the event that you cannot make your scheduled appointment we ask that you give us a 24-hour cancellation notice so that we may accommodate another vela salon and spa client.</p>
    </div>
  </section>

  <section class="panel-menu">
    <h3 class="section-bar left" style="top:0">spa packages</h3>
    <h3 class="section-bar right" style="top:0">massage</h3>
    <p class="note" style="left:18px;top:30px">*All times are approximate. Dressing time and a complimentary foot soak are included.<span class="gap"></span>Create your own experience<br>Choose any combination of your favorite spa experiences and let us do the rest to make it a day to remember. A value of $180 or more includes a complimentary lunch during your visit.</p>
    <p class="note" style="left:190px;top:30px;width:150px">*All times are approximate</p>
    <ul class="menu-list col-left" style="top:57px">
      <li><span class="item">TAKE A BREAK...</span><span class="price">*Approximately 1 1/2 hours $100</span></li>
      <li><span class="item">COUPLES ESCAPE</span><span class="price">*Approximately 1 1/2 hours $140</span></li>
      <li><span class="item">TASTE OF PAMPERING</span><span class="price">*Approximately 2 1/2 hours $154</span></li>
      <li><span class="item">VELA AFTERNOON GETAWAY</span><span class="price">*Approximately 3 hours $180</span></li>
      <li><span class="item">VELA MENTAL RETREAT</span><span class="price">*Approximately 4 hours $240</span></li>
      <li><span class="item">VELA RELAXATION VACATION</span><span class="price">*Approximately 5 hours $335</span></li>
      <li><span class="item">OUR AFTERNOON RENDEZVOUS</span><span class="price">*Approximately 3 1/2 hours $380</span></li>
      <li><span class="item">IMAGINE THE EXPERIENCE</span><span class="price">*Approximately 7 hours $465</span></li>
    </ul>
    <ul class="menu-list col-right" style="top:56px;font-size:3.6px">
      <li style="min-height:17px"><span class="item" style="font-size:3.6px">SWEDISH MASSAGE</span><span class="price">Target Area (*25 min.) $50<br>Full Body (*50 min.) $70<br>Ext. Full Body (*80 min.) $120</span></li>
      <li><span class="item" style="font-size:3.6px">PRENATAL MASSAGE</span><span class="price">Target Areas $50 | Full Body $70</span></li>
      <li><span class="item" style="font-size:3.6px">SEATED MASSAGE</span><span class="price">$25</span></li>
      <li style="min-height:13px"><span class="item" style="font-size:3.6px">FOUR HANDED MASSAGE</span><span class="price">Target (*30 min.) $100<br>Full body (*50 min.) $140</span></li>
      <li><span class="item" style="font-size:3.6px">HOT STONE MASSAGE</span><span class="price">$85 (*80 min.)</span></li>
      <li><span class="item" style="font-size:3.6px">DEEP TISSUE MASSAGE</span><span class="price">$90 (*50 min.)</span></li>
      <li><span class="item" style="font-size:3.6px">SCALP MASSAGE</span><span class="price">$20 (15 min.)</span></li>
      <li><span class="item" style="font-size:3.6px">FOOT MASSAGE</span><span class="price">$20 (15 min.)</span></li>
    </ul>

    <h3 class="section-bar left" style="top:154px">body treatments</h3>
    <h3 class="section-bar right" style="top:154px">facials</h3>
    <ul class="menu-list col-left" style="top:184px">
      <li style="min-height:17px"><span class="item">BODY SCRUBS AND WRAPS</span><span class="price">Scrubs $50 and up<br>Wraps $50 and up<br>Scrub &amp; Wrap $100 and up</span></li>
      <li><span class="item">BACK TREATMENT</span><span class="price">$55</span></li>
      <li><span class="item">SINUS TREATMENT</span><span class="price">$50</span></li>
    </ul>
    <ul class="menu-list col-right facial-list" style="top:182px">
      <li><span class="item">EXPRESS FACIAL</span><span class="price">$50</span></li>
      <li><span class="item">TEEN FACIAL</span><span class="price">$55</span></li>
      <li style="min-height:16px"><span class="item">CUSTOMIZED FACIAL</span><span class="price">Women $70<br>Men with shave consultation $70<br>Extractions $10</span></li>
      <li><span class="item">NATURAL FACIAL PEELS</span><span class="price">(approx. 80 min.) Royal Peel $110<br>Algae Peel $90</span></li>
      <li><span class="item">PUMPKIN FACIAL</span><span class="price">$85</span></li>
      <li><span class="item">RADIANCE RENEWAL FACIAL</span><span class="price">$75</span></li>
      <li><span class="item">SKIN BRIGHTENING FACIAL</span><span class="price">$85</span></li>
      <li><span class="item">MICRODERMABRASION</span><span class="price">Call for pricing</span></li>
      <li style="min-height:16px"><span class="item">CHEMICAL EXFOLIATION / PEELS</span><span class="price">$85 – $150 (Series pricing available)<br>Must have consultation before booking peel. (15 min.) NO CHARGE</span></li>
      <li><span class="item">HOT STONE FACIAL</span><span class="price">$85</span></li>
    </ul>

    <h3 class="section-bar left" style="top:220px">body waxing</h3>
    <ul class="menu-list col-left" style="top:251px">
      <li style="min-height:13px"><span class="item">FULL BODY WAXING</span><span class="price">Lip/Brow/Chin/Sideburns/Stomach<br>$15 each area and up</span></li>
      <li style="min-height:13px"><span class="item"></span><span class="price">Bikini/Under Arms/Forearms<br>start at $25 each service</span></li>
      <li style="min-height:13px"><span class="item"></span><span class="price">Full Legs/Men's Back/Men's Chest<br>$50 each service</span></li>
      <li><span class="item"></span><span class="price">Half Legs/Full Arms $30 each service</span></li>
      <li><span class="item"></span><span class="price">Brazilian Wax $75 and up</span></li>
    </ul>

    <h3 class="section-bar left" style="top:309px">hair</h3>
    <h3 class="section-bar right" style="top:309px">hair extentions</h3>
    <ul class="menu-list col-left" style="top:339px">
      <li style="min-height:17px"><span class="item">CUTS</span><span class="price">Women $34 and up | Men $21 and up<br>Student $21 and up | Child (0-11) $15 and up<br>Bang Trim $15 and up</span></li>
      <li style="min-height:12px"><span class="item">STYLE</span><span class="price">Formal $45 and up | Bride $55 and up<br>Casual $18 and up</span></li>
      <li style="min-height:12px"><span class="item">FOILS</span><span class="price">Full $55 and up | Half $45 and up<br>Face $35 and up</span></li>
      <li><span class="item">COLOR</span><span class="price">All Over Color $48 and up</span></li>
      <li><span class="item">PERM</span><span class="price">Regular $65 and up</span></li>
      <li><span class="item">RELAXERS</span><span class="price">Regular $75 and up</span></li>
    </ul>
    <ul class="menu-list col-right" style="top:339px">
      <li><span class="item" style="font-size:3.6px">HUMAN HAIR EXTENSIONS</span><span class="price">Call for consultation and pricing</span></li>
      <li><span class="item" style="font-size:3.6px">HAIR PIECES</span><span class="price">Call for consultation and pricing</span></li>
      <li><span class="item" style="font-size:3.6px">EYELASH EXTENSIONS</span><span class="price">Call for consultation and pricing</span></li>
    </ul>

    <h3 class="section-bar right" style="top:376px">make up</h3>
    <ul class="menu-list col-right" style="top:407px">
      <li style="min-height:12px"><span class="item" style="font-size:3.6px">INCLUDES COMPLIMENTARY MASCARA</span><span class="price">application $40<br>application with lesson $70</span></li>
      <li><span class="item" style="font-size:3.6px">EYELASH AND EYEBROW TINTING</span><span class="price">Call for Pricing</span></li>
    </ul>

    <h3 class="section-bar left" style="top:463px">hands and feet</h3>
    <ul class="menu-list col-left" style="top:495px">
      <li><span class="item">ULTIMATE PEDICURE</span><span class="price">$75 | French $80</span></li>
      <li><span class="item">MANICURE</span><span class="price">$22-$24 | French $27 and up</span></li>
      <li><span class="item">SPA MANICURE</span><span class="price">$32-$34 | French $37 and up</span></li>
      <li><span class="item">PEDICURE</span><span class="price">$52-$54 | French $57 and up</span></li>
      <li><span class="item">SPA PEDICURE</span><span class="price">$62-$64 | French $67 and up</span></li>
      <li><span class="item">TOES TO GO</span><span class="price">$35 | French $40 and up</span></li>
      <li><span class="item">POLISH CHANGE</span><span class="price">Fingers $10 | Toes $15 + $5 for French</span></li>
      <li><span class="item">BUFF/POLISH</span><span class="price">Fingers $15 | Toes $20 + $5 for French</span></li>
      <li style="min-height:17px"><span class="item">ARTIFICIAL NAILS</span><span class="price">Full Set $50 and up | Fill In $30 and up<br>Nail Wrap $50 | Repair $6 and up<br>Soak Off $15</span></li>
      <li><span class="item">NAIL ART</span><span class="price">$5 and up</span></li>
    </ul>

    <div class="contact-box">
      <div class="brand"><span>Vela Salon Spa</span></div>
      <div class="contact-details">
        <p>www.velasalonspa.com</p>
        <p>hello@velasalonspa.com</p>
        <p>418 MAPLE RIDGE ROAD, HARLOW<br>OHIO 45012 USA</p>
        <p>555-VELASPA (835 2772)</p>
      </div>
    </div>
  </section>

  <section class="panel-front">
    <div class="photo-frame"><div class="photo" role="img" aria-label="Photo of a stylist trimming a client's hair"></div></div>
    <div class="brand"><span>Vela</span><span>Salon Spa</span></div>
  </section>
  <p class="view-label">front</p>

  <div class="sleeve-edge l"></div>
  <div class="sleeve-edge r"></div>
  <section class="sleeve-cover">
    <div class="photo-frame"><div class="photo" role="img" aria-label="Photo of a stylist trimming a client's hair"></div></div>
    <div class="brand"><span>Vela</span><span>Salon Spa</span></div>
  </section>
  <div class="sleeve"></div>

</div>
</body>
</html>
```